Summit Brightway Realty Group & Greenleaf Lending Services, Inc.
Present Our
Annual Holiday Celebration

for Agents, Originators, Clients & Friends
All are Welcome!!

Catered by Chef Ramo Ramo
w/ DJ and Full Dance Floor

** No Cover Charge
Saturday, January 22, 2022
7 pm - 11 pm

at Velvet Parlor
4871 Q Street NE Washington DC 20019

Call Marcus Pelletier at (240) 555-0184 with questions.

```html
<!DOCTYPE html>
<html lang="en">
<head>
<meta charset="utf-8">
<title>Annual Holiday Celebration</title>
<link rel="stylesheet" href="https://fonts.googleapis.com/css2?family=Bebas+Neue&family=Oswald:wght@400;500&family=Allura&display=swap">
<style>
  :root {
    --page: #d0d1d5;
    --purple: #4f2a86;
    --violet: #7a2590;
    --magenta: #c01b88;
    --gold: #fdb515;
    --orange: #f07e12;
    --white: #ffffff;
    --red: #e0183f;
    --ink: #1f2a44;
    --green: #2f7d3a;
    --photo-a: #e9b9c9;
    --photo-b: #b45a8e;
  }
  * { box-sizing: border-box; margin: 0; padding: 0; }
  html, body { width: 1200px; height: 1149px; overflow: hidden; background: var(--page); }

  .flyer {
    position: absolute; left: 80px; top: 54px; width: 1040px; height: 1040px;
    overflow: hidden;
    background: linear-gradient(125deg, var(--purple) 0%, var(--violet) 45%, var(--magenta) 100%);
    font-family: "Bebas Neue", sans-serif;
    color: var(--white);
  }

  .portrait {
    position: absolute; left: 555px; top: 48px; width: 485px; height: 992px;
    border-radius: 240px 0 0 0;
    background: radial-gradient(ellipse at 55% 30%, var(--photo-a) 0%, var(--photo-b) 70%, rgba(180,90,142,0.4) 100%);
  }

  .sponsors {
    position: absolute; left: 52px; top: 0; width: 482px; height: 156px;
    background: var(--white);
    display: flex; align-items: center; justify-content: space-around; padding: 0 18px;
  }
  .sponsor {
    display: flex; align-items: center; gap: 10px;
    font-family: "Oswald", sans-serif; font-weight: 500; font-size: 17px; line-height: 1.15;
    color: var(--ink); text-transform: uppercase; width: 210px;
  }
  .sponsor-mark { width: 22px; height: 22px; flex: none; background: var(--ink); }
  .sponsor-mark.round { border-radius: 50%; background: var(--green); }

  .kicker {
    position: absolute; left: 49px; top: 190px;
    font-size: 64px; letter-spacing: 6px; line-height: 1;
  }
  .headline {
    position: absolute; left: 52px; top: 264px;
    font-size: 146px; line-height: 1; letter-spacing: -1px; font-weight: 400;
    color: var(--gold);
    text-shadow: 0 3px 0 var(--orange), 0 0 12px rgba(253,181,21,0.4);
    white-space: nowrap;
  }
  .celebration {
    position: absolute; left: 51px; top: 402px;
    font-size: 62px; letter-spacing: 23px; line-height: 1;
  }
  .audience {
    position: absolute; left: 49px; top: 479px; width: 737px; height: 52px;
    background: linear-gradient(90deg, var(--gold) 80%, rgba(253,181,21,0.3) 100%);
    border-left: 2px solid var(--white);
    font-size: 44px; line-height: 54px; padding-left: 8px; white-space: nowrap;
  }
  .welcome {
    position: absolute; left: 49px; top: 558px;
    font-size: 68px; letter-spacing: 5px; line-height: 1;
  }
  .no-cover {
    position: absolute; left: 86px; top: 612px;
    font-family: "Allura", cursive; font-size: 98px; line-height: 1;
    color: var(--gold); white-space: nowrap;
  }

  .details {
    position: absolute; left: 49px; top: 753px; width: 421px; height: 190px;
    border: 3px solid var(--white);
    box-shadow: 0 0 10px rgba(255,255,255,0.7), inset 0 0 8px rgba(255,255,255,0.35);
    text-align: center; padding-top: 14px; line-height: 1;
  }
  .details .date { font-size: 48px; letter-spacing: -1px; }
  .details .time { font-size: 48px; letter-spacing: -1px; margin-top: 2px; }
  .details .venue { font-size: 33px; margin-top: 6px; line-height: 0.98; }

  .contact {
    position: absolute; left: 51px; top: 976px;
    font-family: "Oswald", sans-serif; font-weight: 400; font-size: 25px; letter-spacing: -0.3px;
    white-space: nowrap;
  }

  .caterer {
    position: absolute; left: 620px; top: 891px; width: 420px; height: 96px;
    background: var(--white);
    text-align: center; white-space: nowrap; padding-top: 10px;
  }
  .caterer .line { font-size: 44px; line-height: 1; letter-spacing: -0.5px; }
  .caterer .label { color: var(--gold); }
  .caterer .chef { color: var(--red); }
  .caterer .extra { font-size: 26px; line-height: 1; margin-top: 6px; color: var(--violet); letter-spacing: 1px; }
</style>
</head>
<body>
  <main class="flyer">
    <div class="portrait" role="img" aria-label="Portrait photo of the host in a white shirt, smiling, hand at his chin"></div>

    <header class="sponsors">
      <div class="sponsor"><span class="sponsor-mark"></span>Summit Brightway Realty Group</div>
      <div class="sponsor"><span class="sponsor-mark round"></span>Greenleaf Lending Services, Inc.</div>
    </header>

    <p class="kicker">Present our</p>
    <h1 class="headline">ANNUAL HOLIDAY</h1>
    <p class="celebration">CELEBRATION</p>
    <p class="audience">For agents, originators, clients &amp; friends</p>
    <p class="welcome">ALL ARE WELCOME!</p>
    <p class="no-cover">No cover charge</p>

    <section class="details">
      <p class="date">SATURDAY JANUARY 22, 2022</p>
      <p class="time">- 07:00 PM - 11:00 PM -</p>
      <p class="venue">VELVET PARLOR 4871 Q STREET NE<br>WASHINGTON DC 20019</p>
    </section>

    <p class="contact">Call Marcus Pelletier at (240) 555-0184 with questions</p>

    <div class="caterer">
      <p class="line"><span class="label">CATERED BY: </span><span class="chef">CHEF RAMO RAMO</span></p>
      <p class="extra">W/ DJ AND FULL DANCE FLOOR</p>
    </div>
  </main>
</body>
</html>
```